Event flyer for Sunday night Youth Group

Need a 4 x 6 or 5 x 7 flyer for a new youth group starting on April 14. The youth group is for students in middle school and high school so it needs to look fun and cool, but not childish. I prefer it not to include pictures of people unless it's so obscure you can't really see their faces. I've uploaded some pictures of flyers I like. I've also attached a couple versions of our logo to use on the flyer.
Information the flyer needs to include:
Youth Group
Sundays, 6-8pm (beginning April 14)
Location: Merriwick's - 4219 Hollowfern Ln S, Keizer, 97418
There will be dinner, games, friends, and a message.
Target Market(s)
Youth ages 13-18
Industry/Entity Type
Church
Colors
Designer to choose colors to be used in the design.
Look and feel

```html
<!DOCTYPE html>
<html lang="en">
<head>
<meta charset="utf-8">
<title>Youth Group Flyer</title>
<link rel="stylesheet" href="https://fonts.googleapis.com/css2?family=Lobster&family=Oswald:wght@500&family=Open+Sans:wght@300;400;700;800&family=Montserrat:wght@500&display=swap">
<style>
  :root {
    --backdrop: #d3cbc6;
    --paper: #ffffff;
    --youth-blue: #1fa6e0;
    --group-white: #ffffff;
    --splash-grey: #b9b9bd;
    --ink-black: #161616;
    --band-purple: #3a1f5c;
    --stage-pink: #c8237a;
    --stage-dark: #2a0f2e;
    --crowd-violet: #4a3cb8;
    --crowd-deep: #231a5e;
    --slate: #24414a;
    --sage: #7f8c7a;
  }
  * { margin: 0; padding: 0; box-sizing: border-box; }
  html, body { width: 1200px; height: 1024px; overflow: hidden; }
  body { background: var(--backdrop); display: flex; align-items: center; justify-content: center; }

  .flyer {
    position: relative;
    width: 665px;
    height: 940px;
    background: var(--paper);
    overflow: hidden;
  }
  .concert-photo {
    position: absolute;
    inset: 0 0 auto 0;
    height: 800px;
    background:
      linear-gradient(to bottom, rgba(255,255,255,0) 72%, var(--paper) 96%),
      radial-gradient(ellipse 55% 30% at 40% 28%, var(--stage-pink), rgba(200,35,122,0) 70%),
      linear-gradient(to bottom, var(--stage-dark) 0%, #5a1f6a 28%, var(--crowd-violet) 48%, var(--crowd-deep) 78%, #1a1430 90%);
  }

  .title { position: absolute; inset: 0; pointer-events: none; }
  .title-youth {
    position: absolute;
    left: 140px; top: 40px;
    font: 400 210px/1 "Lobster", cursive;
    color: var(--youth-blue);
    transform: rotate(-11deg);
    transform-origin: left bottom;
    letter-spacing: -4px;
  }
  .title-group {
    position: absolute;
    left: 300px; top: 200px;
    font: 400 96px/1 "Lobster", cursive;
    color: var(--group-white);
    transform: rotate(-11deg);
    letter-spacing: -2px;
  }

  .schedule {
    position: absolute;
    left: 372px; top: 298px;
    width: 280px; height: 110px;
  }
  .schedule-splash { position: absolute; inset: 0; }
  .schedule-text {
    position: absolute;
    left: 22px; top: 20px;
    font: 500 33px/1.08 "Oswald", sans-serif;
    color: var(--ink-black);
    transform: rotate(-2deg);
    letter-spacing: -0.5px;
  }

  .venue-band {
    position: absolute;
    left: -20px; top: 462px;
    width: 720px; height: 64px;
    background: rgba(58,31,92,0.88);
    transform: rotate(4deg);
    display: flex; align-items: center;
    padding-left: 85px;
    color: #fff;
    white-space: nowrap;
  }
  .venue-name { font: 800 32px/1 "Open Sans", sans-serif; margin-right: 10px; }
  .venue-address { font: 300 22px/1 "Open Sans", sans-serif; }

  .details {
    position: absolute;
    left: 0; right: 0; top: 774px;
    text-align: center;
    font: 400 19px/1 "Open Sans", sans-serif;
    color: var(--slate);
  }
  .details-accent {
    font-weight: 700;
    font-size: 23px;
    letter-spacing: 3px;
    color: var(--sage);
    margin-left: 8px;
  }

  .church {
    position: absolute;
    left: 0; right: 0; top: 848px;
    display: flex; align-items: center; justify-content: center;
    gap: 14px;
  }
  .church-mark { width: 22px; height: 22px; background: var(--slate); }
  .church-name {
    font: 500 30px/1 "Montserrat", sans-serif;
    color: var(--slate);
    letter-spacing: 1px;
  }
</style>
</head>
<body>
  <main class="flyer">
    <div class="concert-photo" role="img" aria-label="Blurred concert photo: a stage lit in pink and magenta above a large crowd in violet light, fading to white at the bottom"></div>

    <h1 class="title">
      <span class="title-youth">Youth</span>
      <span class="title-group">Group</span>
    </h1>

    <div class="schedule">
      <svg class="schedule-splash" viewBox="0 0 280 110" aria-hidden="true">
        <path d="M14 22 Q40 8 80 14 Q130 4 180 10 Q230 2 262 14 Q278 40 270 62 Q276 90 250 98 Q200 108 150 100 Q100 110 50 102 Q16 104 8 80 Q2 50 14 22 Z" fill="var(--splash-grey)"/>
      </svg>
      <p class="schedule-text">Sundays, 6-8pm<br>(beginning April 14)</p>
    </div>

    <div class="venue-band">
      <span class="venue-name">Merriwick's</span>
      <span class="venue-address">4219 Hollowfern Ln S, Keizer, 97418</span>
    </div>

    <p class="details">There will be dinner, games, friends, and <span class="details-accent">a message</span></p>

    <div class="church">
      <span class="church-mark" aria-hidden="true"></span>
      <span class="church-name">Lanternway Fellowship</span>
    </div>
  </main>
</body>
</html>
```